Website Revamp: Favorzo.com

Just got a new logo looking for a web design to go with the business. I need the photoshop files and stock photos. No Word Press Please.

```html
<!DOCTYPE html>
<html lang="en">
<head>
<meta charset="utf-8">
<title>Favorzo Auto Recycling</title>
<link href="https://fonts.googleapis.com/css2?family=Montserrat:wght@400;500;600;700;800&family=Cinzel:wght@500;600&display=swap" rel="stylesheet">
<style>
:root{
  --green:#7cc242;
  --green-pale:#eef7e6;
  --orange:#f7861b;
  --ink:#1e1e1e;
  --text:#333;
  --topbar:#3d3d3d;
  --footer:#262626;
  --footer-bottom:#1c1c1c;
  --white:#fff;
}
*{margin:0;padding:0;box-sizing:border-box}
html,body{width:1200px;height:2971px;overflow:hidden}
body{position:relative;font-family:"Montserrat",sans-serif;color:var(--text);background:var(--white)}
.abs{position:absolute}

/* top bar */
.topbar{left:0;top:0;width:1200px;height:31px;background:var(--topbar);color:var(--white);font-size:14px}
.topbar .welcome{left:85px;top:7px}
.topbar .contact{top:7px;display:flex;align-items:center;gap:7px}
.topbar svg{width:13px;height:13px;fill:var(--green)}

/* nav */
.nav{left:0;top:31px;width:1200px;height:112px;background:var(--white)}
.nav a{position:absolute;top:66px;font-size:16px;font-weight:500;color:var(--ink);text-decoration:none;letter-spacing:.3px}
.nav a.active{color:var(--green)}
.nav .active-line{left:105px;top:109px;width:60px;height:3px;background:var(--green)}
.quote-btn{left:972px;width:142px;height:34px;border-radius:17px;background:var(--green);color:var(--white);font-size:14px;font-weight:700;display:flex;align-items:center;justify-content:center}
.brand-tab{left:517px;top:31px;width:166px;height:144px;background:var(--white);border-radius:0 0 8px 8px;z-index:3;display:flex;flex-direction:column;align-items:center;padding-top:14px}
.brand-tab .mark{width:74px;height:74px;border-radius:50%;background:var(--green)}
.brand-tab .name{margin-top:8px;font-size:24px;font-weight:800;color:var(--green);letter-spacing:1px}

/* hero */
.hero{left:0;top:143px;width:1200px;height:425px;background:linear-gradient(100deg,#5d6670 0%,#4a525b 40%,#3a3034 65%,#6a2630 80%,#3c3f47 100%)}
.hero h1{left:85px;top:152px;font-size:48px;font-weight:800;color:var(--white);text-shadow:0 2px 6px rgba(0,0,0,.5)}
.hero h2{left:85px;top:221px;font-size:30px;font-weight:700;color:var(--white);text-shadow:0 2px 6px rgba(0,0,0,.5)}
.dots{left:85px;top:350px;display:flex;gap:12px}
.dots span{width:11px;height:11px;background:var(--white)}
.dots span.on{background:var(--green);outline:2px solid var(--white);width:13px;height:13px;margin-top:-1px}

/* section titles */
.sec-title{left:0;width:1200px;text-align:center;font-size:26px;font-weight:700;color:var(--ink)}
.rule{left:523px;width:154px;height:3px;background:var(--green)}

/* welcome */
.intro{left:250px;top:697px;width:700px;text-align:center;font-size:16px;line-height:27px;color:var(--ink)}
.feature{top:800px;width:180px;text-align:center}
.feature .badge{width:146px;height:146px;margin:0 auto;border-radius:50%;background:var(--green-pale);border:4px solid var(--green)}
.feature p{margin-top:26px;font-size:19px;font-weight:600;color:var(--ink)}

/* experts band */
.experts{left:0;top:1070px;width:1200px;height:304px;background:radial-gradient(ellipse at 50% 110%,#4a6f99 0%,#1e3a5c 45%,#0f1f36 100%)}
.experts h3{left:0;top:62px;width:1200px;text-align:center;font-family:"Cinzel",serif;font-size:30px;font-weight:600;color:var(--white);letter-spacing:1px}
.experts p{left:150px;top:110px;width:900px;text-align:center;font-size:14px;line-height:27px;font-weight:500;color:var(--white)}
.field{top:193px;height:40px;background:var(--white);border-radius:3px;font-size:13px;color:#444;padding:13px 17px}
.subscribe{left:774px;top:193px;width:182px;height:40px;border-radius:20px;background:var(--orange);color:var(--white);font-size:14px;font-weight:700;display:flex;align-items:center;justify-content:center}

/* services */
.svc-photo{top:1554px;width:322px;height:234px;border:4px solid var(--white);box-shadow:0 0 3px rgba(0,0,0,.35)}
.svc h4{position:absolute;top:1826px;font-size:17px;font-weight:700;color:var(--green);letter-spacing:.2px;white-space:nowrap}
.svc p{position:absolute;top:1866px;width:320px;font-size:13.5px;line-height:21px;color:var(--text)}
.read{position:absolute;top:1956px;width:138px;height:38px;border-radius:19px;background:var(--orange);color:var(--white);font-size:14px;font-weight:700;display:flex;align-items:center;justify-content:center}

/* reviews */
.reviews{left:0;top:2079px;width:1200px;height:556px;background:linear-gradient(110deg,#3a3a3a 0%,#2b2b2b 45%,#1f1f1f 70%,#3b2626 100%)}
.reviews h3{left:0;top:50px;width:1200px;text-align:center;font-size:34px;font-weight:500;color:var(--white);letter-spacing:.5px}
.card{background:#ebebe8;border-radius:12px;color:#333;font-size:10px;line-height:17px;padding:26px 20px 26px 28px}
.card.feat{background:var(--green);color:var(--white);font-size:12px;line-height:21px;font-weight:500;padding:30px 18px 30px 42px}
.card .q{position:absolute;left:0;width:100%;text-align:center;font-size:46px;line-height:1;color:var(--white);font-family:Georgia,serif;font-weight:700}
.card::after{content:"";position:absolute;left:50%;bottom:-9px;margin-left:-9px;border-left:9px solid transparent;border-right:9px solid transparent;border-top:9px solid #ebebe8}
.card.feat::after{border-top-color:var(--green)}
.avatar{border-radius:50%;background:linear-gradient(#c9b8a8,#7a6a5c);border:2px solid var(--white)}
.rname{font-size:14px;font-weight:600;color:var(--white);letter-spacing:.5px;text-align:center;width:200px}

/* footer */
.footer{left:0;top:2635px;width:1200px;height:291px;background:var(--footer);color:var(--white)}
.footer .brand{left:85px;top:50px;display:flex;align-items:center;gap:10px}
.footer .brand .mark{width:22px;height:22px;border-radius:50%;background:var(--green)}
.footer .brand .name{font-size:28px;font-weight:800;color:var(--green)}
.footer .about{left:86px;top:189px;width:250px;font-size:14px;line-height:21px}
.footer .divider{top:50px;width:1px;height:170px;background:#444}
.footer h5{position:absolute;top:69px;font-size:18px;font-weight:500}
.footer .hr{position:absolute;top:104px;width:66px;height:2px;background:var(--green)}
.footer ul{position:absolute;top:127px;list-style:none;font-size:14px;line-height:26.5px}
.footer ul li{display:flex;align-items:center;gap:8px}
.footer ul svg{width:13px;height:13px;fill:var(--green);flex:none}
.social{left:982px;top:124px;display:flex;gap:8px}
.social span{width:27px;height:27px;border-radius:50%;background:var(--green)}
.copy{left:0;top:2926px;width:1200px;height:45px;background:var(--footer-bottom);color:var(--white);font-size:13px;text-align:center;padding-top:15px}
.copy b{color:var(--green);font-weight:500}
</style>
</head>
<body>

<!-- top bar -->
<div class="abs topbar">
  <span class="abs welcome">Welcome to Favorzo Auto Recycling !</span>
  <span class="abs contact" style="left:836px">
    <svg viewBox="0 0 24 24"><path d="M6.6 10.8a15 15 0 0 0 6.6 6.6l2.2-2.2a1 1 0 0 1 1-.25 11.4 11.4 0 0 0 3.6.57 1 1 0 0 1 1 1V20a1 1 0 0 1-1 1A17 17 0 0 1 3 4a1 1 0 0 1 1-1h3.5a1 1 0 0 1 1 1c0 1.25.2 2.45.57 3.6a1 1 0 0 1-.25 1z"/></svg>555-014-2287</span>
  <span class="abs contact" style="left:982px">
    <svg viewBox="0 0 24 24"><path d="M12 2 2 8v12h20V8zm0 2.3L19.5 9 12 13.5 4.5 9z"/></svg>info@favorzo.com</span>
</div>

<!-- nav -->
<nav class="abs nav">
  <a class="active" style="left:111px">HOME</a>
  <div class="abs active-line"></div>
  <a style="left:222px">ABOUT US</a>
  <a style="left:370px">SERVICES</a>
  <a style="left:727px">NEWS</a>
  <a style="left:825px;top:64px">CONTACT US</a>
  <div class="abs quote-btn" style="top:52px">GET A QUOTE</div>
</nav>
<div class="abs brand-tab">
  <div class="mark"></div>
  <div class="name">FAVORZO</div>
</div>

<!-- hero -->
<section class="abs hero" role="img" aria-label="Stacked scrapped cars under a cloudy grey sky">
  <h1 class="abs">Recycle your Car Today!</h1>
  <h2 class="abs">Get cash for your old car!</h2>
  <div class="abs dots"><span class="on"></span><span></span><span></span><span></span></div>
</section>

<!-- welcome -->
<h2 class="abs sec-title" style="top:620px">WELCOME TO FAVORZO</h2>
<div class="abs rule" style="top:670px"></div>
<p class="abs intro">Do you have an old car that you’re ready to get rid of? Whether it’s<br>in good condition or not, we’ll take it!</p>

<div class="abs feature" style="left:154px">
  <div class="badge" role="img" aria-label="Car icon"></div>
  <p>Recycling Cars</p>
</div>
<div class="abs feature" style="left:391px">
  <div class="badge" role="img" aria-label="Truck icon"></div>
  <p>Trucks &amp; Buses</p>
</div>
<div class="abs feature" style="left:631px">
  <div class="badge" role="img" aria-label="Motorbike icon"></div>
  <p>Two wheelers</p>
</div>
<div class="abs feature" style="left:870px">
  <div class="badge" role="img" aria-label="Cargo ship icon"></div>
  <p>Cargo Scraps</p>
</div>

<!-- experts -->
<section class="abs experts" role="img" aria-label="Dark blue close-up of a car bonnet with light rays">
  <h3 class="abs">WE ARE THE INDUSTRY EXPERTS!</h3>
  <p class="abs">Dedicated to taking action the Meadow Alliance was created to help bring adaption strategies to life. Working<br>with local communities we are committed to implementing strategies that will sustain communities..</p>
  <div class="abs field" style="left:242px;width:219px">Name</div>
  <div class="abs field" style="left:480px;width:276px">Email</div>
  <div class="abs subscribe">SUBSCRIBE NOW</div>
</section>

<!-- services -->
<h2 class="abs sec-title" style="top:1447px">OUR SERVICES</h2>
<div class="abs rule" style="top:1497px"></div>

<div class="abs svc-photo" style="left:85px;background:linear-gradient(#b9c4cc,#30343c 60%,#555)" role="img" aria-label="Wrecked dark car on a flatbed tow truck"></div>
<div class="abs svc-photo" style="left:440px;background:radial-gradient(circle at 40% 45%,#e8e8e8,#8c8c8c 55%,#3a3a3a)" role="img" aria-label="Assorted metal car parts, brake discs and pulleys"></div>
<div class="abs svc-photo" style="left:791px;background:linear-gradient(#2f7fd0 0%,#6aa9e0 45%,#8a4a3a 70%,#5a4a40)" role="img" aria-label="Crane grabber above a pile of scrap cars under blue sky"></div>

<div class="svc">
  <h4 style="left:85px">DOORSTEP TOWING</h4>
  <p style="left:87px">Nemo enim ipsam voluptatem quia voluptas sit aspernatur aut odit aut fugit, sed quia con­sequuntur magni dolores.</p>
  <div class="read" style="left:86px">READ MORE</div>
  <h4 style="left:440px">MATERIAL SELECTION</h4>
  <p style="left:441px">Nemo enim ipsam voluptatem quia voluptas sit aspernatur aut odit aut fugit, sed quia con­sequuntur magni dolores eo.</p>
  <div class="read" style="left:441px">READ MORE</div>
  <h4 style="left:789px">RECYCLING SCRAPS &amp; VEHICLES</h4>
  <p style="left:793px">Nemo enim ipsam voluptatem quia voluptas sit aspernatur aut odit aut fugit, sed quia con­sequuntur magni dolores eos..</p>
  <div class="read" style="left:793px">READ MORE</div>
</div>

<!-- reviews -->
<section class="abs reviews" role="img" aria-label="Dim workshop scene with a mechanic beside a car">
  <h3 class="abs">CUSTOMER REVIEWS</h3>

  <div class="abs card" style="left:145px;top:165px;width:240px;height:183px">Nemo enim ipsam voluptatem quia voluptas sit aspernatur aut odit aut fugit, sed quia consequuntur magni dolores eos qui ratione voluptatem sequi nesciunt.<span class="q" style="top:138px">”</span></div>
  <div class="abs card feat" style="left:448px;top:125px;width:303px;height:231px">Nemo enim ipsam voluptatem quia voluptas sit aspernatur aut odit aut fugit, sed quia consequuntur magni dolores eos qui ratione voluptatem sequi nesciunt. Neque porro quisquam est, qui dolorem ipsum quia dolor sit amet, consectetur, adipisci velit,<span class="q" style="top:186px">”</span></div>
  <div class="abs card" style="left:813px;top:165px;width:240px;height:183px">Nemo enim ipsam voluptatem quia voluptas sit aspernatur aut odit aut fugit, sed quia consequuntur magni dolores eos qui ratione voluptatem sequi nesciunt. Neque porro quisqu­am est, qui dolorem<span class="q" style="top:138px">”</span></div>

  <div class="abs avatar" style="left:230px;top:375px;width:66px;height:66px" role="img" aria-label="Customer portrait"></div>
  <div class="abs avatar" style="left:554px;top:395px;width:84px;height:84px" role="img" aria-label="Customer portrait"></div>
  <div class="abs avatar" style="left:897px;top:375px;width:66px;height:66px" role="img" aria-label="Customer portrait"></div>
  <div class="abs rname" style="left:160px;top:456px">DANA REYES</div>
  <div class="abs rname" style="left:495px;top:490px">OWEN BLAKE</div>
  <div class="abs rname" style="left:831px;top:456px">MILO GRANT</div>
</section>

<!-- footer -->
<footer class="abs footer">
  <div class="abs brand"><span class="mark"></span><span class="name">FAVORZO</span></div>
  <p class="abs about">Dedicated to taking action the Meadow Alliance was created to help bring adaption strategies to life.</p>

  <div class="abs divider" style="left:361px"></div>
  <div class="abs divider" style="left:598px"></div>
  <div class="abs divider" style="left:932px"></div>

  <h5 style="left:419px">Quick Links</h5><div class="hr" style="left:419px"></div>
  <ul style="left:419px"><li>Home</li><li>About Us</li><li>Services</li><li>News</li><li>Contact Us</li></ul>

  <h5 style="left:680px">Contact</h5><div class="hr" style="left:680px"></div>
  <ul style="left:680px">
    <li><svg viewBox="0 0 24 24"><path d="M6.6 10.8a15 15 0 0 0 6.6 6.6l2.2-2.2a1 1 0 0 1 1-.25 11.4 11.4 0 0 0 3.6.57 1 1 0 0 1 1 1V20a1 1 0 0 1-1 1A17 17 0 0 1 3 4a1 1 0 0 1 1-1h3.5a1 1 0 0 1 1 1c0 1.25.2 2.45.57 3.6a1 1 0 0 1-.25 1z"/></svg>555-014-2287</li>
    <li><svg viewBox="0 0 24 24"><path d="M12 2 2 8v12h20V8zm0 2.3L19.5 9 12 13.5 4.5 9z"/></svg>hello@favorzo.com</li>
    <li style="align-items:flex-start"><svg viewBox="0 0 24 24" style="margin-top:6px"><path d="M12 2a7 7 0 0 0-7 7c0 5 7 13 7 13s7-8 7-13a7 7 0 0 0-7-7zm0 9.5A2.5 2.5 0 1 1 12 6.5a2.5 2.5 0 0 1 0 5z"/></svg><span>2140 Harbor Lane, Fairview<br>OR 97024</span></li>
  </ul>

  <h5 style="left:982px">Follow Us</h5>
  <div class="abs social"><span></span><span></span><span></span><span></span></div>
</footer>
<div class="abs copy"><b>Favorzo</b> &nbsp;© Copyrights.2020. All rights reserved.</div>

</body>
</html>
```